Business Card Design

I will be finding aged care homes for those who need placement.
Assisting with all of the paperwork.
I would like Australian wattle picture on the card/ logo please
Industry/Entity Type
Business
Contact Information for Business Card
Senior Living Pathways
Marla Jensen
PH: 0438 926 153
Email: seniorlivingpathways@mailbox.example
ABN: 63 214 958 307
PO Box 3189, Kallangur QLD 4503

```html
<!DOCTYPE html>
<html lang="en">
<head>
<meta charset="utf-8">
<title>Senior Living Pathways – Business Card</title>
<link rel="stylesheet" href="https://fonts.googleapis.com/css2?family=EB+Garamond:wght@400;500;700&display=swap">
<style>
  :root {
    --card-white: #ffffff;
    --card-green: #008850;
    --wattle-yellow: #f8c700;
    --ink-black: #111111;
    --text-white: #ffffff;
  }
  html, body {
    margin: 0;
    padding: 0;
    width: 1200px;
    height: 741px;
    overflow: hidden;
    background: var(--card-white);
  }
  .card {
    position: relative;
    width: 1200px;
    height: 741px;
    overflow: hidden;
    background: var(--card-white);
    font-family: "EB Garamond", Garamond, serif;
  }
  .brand-panel {
    position: absolute;
    left: 0;
    top: 0;
    width: 456px;
    height: 741px;
    background: var(--card-white);
  }
  .brand-dot {
    position: absolute;
    left: 162px;
    top: 118px;
    width: 150px;
    height: 150px;
    border-radius: 50%;
    background: var(--wattle-yellow);
  }
  .brand-name {
    position: absolute;
    left: 0;
    width: 456px;
    margin: 0;
    text-align: center;
    font-weight: 400;
    font-size: 68px;
    line-height: 1;
    color: var(--ink-black);
  }
  .brand-name span {
    position: absolute;
    left: 0;
    width: 100%;
  }
  .contact-panel {
    position: absolute;
    left: 456px;
    top: 0;
    width: 744px;
    height: 741px;
    background: var(--card-green);
    color: var(--text-white);
  }
  .line {
    position: absolute;
    left: 27px;
    margin: 0;
    line-height: 1;
    white-space: nowrap;
  }
  .person-name {
    top: 78px;
    font-size: 64px;
    font-weight: 700;
    color: var(--wattle-yellow);
  }
  .detail { font-size: 46px; font-weight: 400; }
  .detail b { font-weight: 700; }
  .email-address { font-size: 41px; }
  .postal { font-size: 48px; font-weight: 700; }
</style>
</head>
<body>
  <div class="card">
    <section class="brand-panel">
      <div class="brand-dot" aria-hidden="true"></div>
      <h1 class="brand-name">
        <span style="top:374px">Senior</span>
        <span style="top:484px">Living</span>
        <span style="top:589px">Pathways</span>
      </h1>
    </section>
    <section class="contact-panel">
      <h2 class="line person-name">Marla Jensen</h2>
      <p class="line detail" style="top:221px"><b>PH:</b> 0438 926 153</p>
      <p class="line detail" style="top:281px"><b>Email:</b></p>
      <p class="line detail email-address" style="top:349px">seniorlivingpathways@mailbox.example</p>
      <p class="line detail" style="top:407px"><b>ABN:</b> 63 214 958 307</p>
      <p class="line postal" style="top:534px">PO Box 3189</p>
      <p class="line postal" style="top:606px">Kallangur QLD 4503</p>
    </section>
  </div>
</body>
</html>
```